Fresh Gear Falcon - Packaging Design

We need a package design for our Fresh Gear Falcon deodorant balls. This needs to be a print ready design front and back. The package is 4 1/4 inches wide and 5 inches tall. The product is called Fresh Gear Falcons and are geared towards martial arts students to stick into their gear bags to keep them from smelling.

Target Market(s)

martial artists, boxers, athletes

Font styles to use
Sans Serif

Requirements
Must have
• Logo and name

```html
<!DOCTYPE html>
<html lang="en">
<head>
<meta charset="utf-8">
<title>Fresh Gear Falcon – Blister Card Front and Back</title>
<link rel="stylesheet" href="https://fonts.googleapis.com/css2?family=Montserrat:wght@500;600;700;800&display=swap">
<style>
  :root {
    --bg: #e4e4e5;
    --ink: #0b0b0b;
    --orange: #f47a20;
    --orange-deep: #d9541d;
    --white: #ffffff;
    --hole: #d8d8d8;
    --ball-light: #fbc43a;
    --ball-dark: #d99210;
  }
  * { box-sizing: border-box; margin: 0; padding: 0; }
  html, body { width: 1200px; height: 1200px; overflow: hidden; }
  body {
    background: var(--bg);
    font-family: "Montserrat", sans-serif;
    position: relative;
  }
  .card {
    position: absolute;
    top: 238px;
    width: 507px;
    height: 828px;
    border-radius: 22px;
    overflow: hidden;
    box-shadow: 0 4px 14px rgba(0,0,0,.25);
  }
  .card--front { left: 76px; background: var(--ink); }
  .card--back {
    left: 618px;
    background: radial-gradient(ellipse at 60% 85%, #2e2e2e 0%, #141414 45%, var(--ink) 75%);
  }
  .card__bg { position: absolute; inset: 0; }
  .hang-hole {
    position: absolute;
    z-index: 3;
    left: 190px; top: 34px;
    width: 126px; height: 28px;
    border-radius: 6px;
    background: var(--hole);
    box-shadow: inset 0 2px 3px rgba(0,0,0,.2);
  }
  .mascot {
    position: absolute;
    background: radial-gradient(circle at 50% 40%, #5a5a5a 0%, #333 55%, #1d1d1d 100%);
  }
  .mascot--front {
    left: 100px; top: 70px; width: 290px; height: 250px;
    border-radius: 48% 48% 40% 40%;
  }
  .mascot--head {
    left: 44px; top: 28px; width: 86px; height: 90px;
    border-radius: 50%;
  }
  .mascot--ghost {
    left: 262px; top: 450px; width: 240px; height: 330px;
    border-radius: 45% 45% 30% 30%;
    background: radial-gradient(circle at 50% 35%, rgba(120,80,50,.35) 0%, rgba(40,30,25,.25) 55%, rgba(0,0,0,0) 80%);
  }
  .brand-name {
    position: absolute;
    z-index: 2;
    color: var(--orange);
    font-weight: 800;
    text-transform: uppercase;
    text-align: center;
    line-height: 0.95;
  }
  .brand-name--front {
    left: 20px; right: 20px; top: 345px;
    font-size: 60px;
  }
  .brand-name--back {
    left: 330px; width: 160px; top: 44px;
    font-size: 22px;
  }
  .tagline {
    position: absolute;
    left: 20px; right: 20px; top: 534px;
    color: var(--white);
    font-size: 12px;
    font-weight: 500;
    line-height: 1.2;
    text-align: center;
  }
  .ball {
    position: absolute;
    border-radius: 50%;
    background: radial-gradient(circle at 38% 30%, #ffe27a 0%, var(--ball-light) 35%, var(--ball-dark) 100%);
  }
  .ball--front { width: 188px; height: 188px; top: 578px; border: 3px solid var(--orange-deep); }
  .ball--front.ball--left { left: 46px; }
  .ball--front.ball--right { left: 270px; }
  .ball--back { width: 192px; height: 192px; top: 578px; }
  .ball--back.ball--left { left: 46px; }
  .ball--back.ball--right { left: 270px; }
  .seal {
    position: absolute;
    width: 72px; height: 72px;
    border-radius: 50%;
    background: var(--ink);
    border: 2px solid #bbb;
  }
  .seal--front { left: 217px; top: 742px; }
  .seal--back { left: 218px; top: 526px; }
  .icons {
    position: absolute;
    top: 148px; left: 0; right: 0; height: 56px;
  }
  .icons svg { position: absolute; top: 0; fill: var(--white); }
  .copy {
    position: absolute;
    left: 46px; width: 420px;
    color: var(--white);
  }
  .copy h2 {
    color: var(--orange);
    font-size: 12px;
    font-weight: 700;
    margin-bottom: 8px;
  }
  .copy p {
    font-size: 9.4px;
    font-weight: 500;
    line-height: 12px;
    margin-bottom: 12px;
  }
  .copy .copy__lead {
    color: var(--orange);
    font-size: 11.5px;
    font-weight: 600;
    line-height: 14px;
    margin: 16px 0 14px -3px;
  }
  .web {
    position: absolute;
    left: 0; right: 0; top: 484px;
    text-align: center;
    color: var(--white);
    font-size: 12px;
    font-weight: 700;
  }
  .web span { color: var(--orange); }
</style>
</head>
<body>

<section class="card card--front" aria-label="Package front">
  <svg class="card__bg" viewBox="0 0 507 828" preserveAspectRatio="none" aria-hidden="true">
    <rect width="507" height="828" fill="var(--ink)"/>
    <polygon points="0,0 507,0 507,118 253,250 0,118" fill="var(--white)"/>
    <polygon points="0,118 253,250 507,118 507,146 253,270 0,146" fill="var(--orange)"/>
    <polygon points="0,146 253,270 507,146 507,152 253,276 0,152" fill="#9a9a9a"/>
  </svg>
  <div class="hang-hole"></div>
  <div class="mascot mascot--front" role="img" aria-label="Mascot illustration: crouching masked martial artist in grey with orange headband"></div>
  <div class="brand-name brand-name--front">Fresh Gear<br>Falcon</div>
  <p class="tagline">Geared Towards Martial Arts Students To Stick Into Their<br>Gear Bags To Keep Them From Smelling.</p>
  <div class="ball ball--front ball--left" role="img" aria-label="Product photo: yellow deodorant ball in blister"></div>
  <div class="ball ball--front ball--right" role="img" aria-label="Product photo: yellow deodorant ball in blister"></div>
  <div class="seal seal--front"></div>
</section>

<section class="card card--back" aria-label="Package back">
  <div class="mascot mascot--ghost" role="img" aria-label="Faint background mascot illustration"></div>
  <div class="hang-hole"></div>
  <div class="mascot mascot--head" role="img" aria-label="Mascot head illustration with orange headband"></div>
  <div class="brand-name brand-name--back">Fresh Gear<br>Falcon</div>

  <div class="icons" aria-label="Use in shoes, bags, drawers and cars">
    <svg style="left:46px" width="84" height="48" viewBox="0 0 84 48" aria-label="Shoe icon" role="img">
      <path d="M4 30 C4 22 8 14 12 8 L22 12 C28 18 36 20 46 20 L70 26 C78 28 82 32 82 36 L82 40 L4 40 Z"/>
      <rect x="2" y="42" width="80" height="4" rx="2"/>
    </svg>
    <svg style="left:179px" width="58" height="48" viewBox="0 0 58 48" aria-label="Bag icon" role="img">
      <path d="M20 4 h18 a3 3 0 0 1 3 3 v5 h-5 v-3 h-14 v3 h-5 v-5 a3 3 0 0 1 3 -3z"/>
      <rect x="1" y="12" width="56" height="34" rx="4"/>
      <rect x="24" y="24" width="10" height="6" fill="var(--ink)"/>
    </svg>
    <svg style="left:292px" width="44" height="58" viewBox="0 0 44 58" aria-label="Drawer icon" role="img">
      <rect x="1" y="1" width="42" height="52" rx="2" fill="none" stroke="var(--white)" stroke-width="2"/>
      <rect x="5" y="5" width="34" height="20" rx="2" fill="none" stroke="var(--white)" stroke-width="2"/>
      <rect x="5" y="29" width="34" height="20" rx="2" fill="none" stroke="var(--white)" stroke-width="2"/>
      <rect x="17" y="12" width="10" height="2"/><rect x="17" y="36" width="10" height="2"/>
    </svg>
    <svg style="left:384px" width="68" height="50" viewBox="0 0 68 50" aria-label="Car icon" role="img">
      <path d="M14 6 h40 l8 14 h4 v20 h-64 v-20 h4 z"/>
      <rect x="8" y="40" width="10" height="8" rx="2"/><rect x="50" y="40" width="10" height="8" rx="2"/>
      <path d="M18 10 h32 l5 10 h-42 z" fill="var(--ink)"/>
      <rect x="8" y="26" width="10" height="5" rx="2" fill="var(--ink)"/>
      <rect x="50" y="26" width="10" height="5" rx="2" fill="var(--ink)"/>
      <rect x="24" y="30" width="20" height="3" fill="var(--ink)"/>
    </svg>
  </div>

  <div class="copy" style="top:237px">
    <h2>What is Lorem Ipsum?</h2>
    <p>Lorem Ipsum is simply dummy text of the printing and typesetting industry. Lorem Ipsum has been the industry's standard dummy text ever since the 1500s, when an unknown printer took a galley of type and scrambled it to make a type specimen book. It has survived not only five centuries, but also the leap into electronic typesetting, remaining essentially unchanged.</p>
    <p>It was popularised in the 1960s with the release of Glyphsheet sheets containing Lorem Ipsum passages, and more recently with desktop publishing software like Inkwell Layout including versions of Lorem Ipsum.</p>
    <p class="copy__lead">Geared Towards Martial Arts Students To Stick Into Their<br>Gear Bags To Keep Them From Smelling.</p>
    <p>It was popularised in the 1960s with the release of Glyphsheet sheets containing Lorem Ipsum passages, and more recently with desktop publishing software like Inkwell Layout including versions of Lorem Ipsum.</p>
  </div>

  <p class="web">www.<span>Fresh Gear Falcon deodorant balls</span>.com</p>
  <div class="seal seal--back"></div>
  <div class="ball ball--back ball--left" role="img" aria-label="Product photo: back of yellow deodorant ball"></div>
  <div class="ball ball--back ball--right" role="img" aria-label="Product photo: back of yellow deodorant ball"></div>
</section>

</body>
</html>
```